Adapt logo for box truck wrap for my restoration company

I need a wrap for our company Harbeck Restoration. We specialize in water damage restoration. I’ve attached our logo, business card, and page header. Things I would like to include are- 24 hour emergency service, our phone number (702)555-0147 and that we do water, fire and mold work. It’s a 2004 Kelvaro Trask which I’ve attached pictures of. I will get the cab wrapped as well.

Industry/Entity Type

Construction- specifically Restoration

Font styles to use
Sans Serif

Colors

Designer to choose colors to be used in the design.

Requirements
Must have
• Water• Fire• Mold, phone number (702)555-0147
Nice to have
• Clean, professional look with the logo

```html
<!DOCTYPE html>
<html lang="en">
<head>
<meta charset="utf-8">
<title>Harbeck Restoration – Box Truck Wrap</title>
<link rel="stylesheet" href="https://fonts.googleapis.com/css2?family=Montserrat:wght@700;800&display=swap">
<style>
  :root {
    --page: #ffffff;
    --frame: #e6e6e6;
    --grey-top: #7a7a7a;
    --grey-bottom: #969696;
    --stripe: #eeeeee;
    --blue-top: #2f9fe8;
    --blue-bottom: #0a6cc4;
    --ink-light: #ffffff;
    --ink-mark: #7b7b7b;
  }
  html, body {
    margin: 0;
    width: 1200px;
    height: 1200px;
    overflow: hidden;
    background: var(--page);
  }
  .canvas {
    width: 1200px;
    height: 1200px;
    display: flex;
    align-items: center;
    justify-content: center;
  }
  .wrap-panel { width: 1100px; height: auto; display: block; }
  .wrap-text {
    font-family: "Montserrat", sans-serif;
    fill: var(--ink-light);
  }
  .hours-number { font-weight: 800; font-size: 84px; letter-spacing: -3px; }
  .hours-label { font-weight: 700; font-size: 16.5px; }
  .company-name { font-weight: 800; font-size: 50px; }
  .company-phone { font-weight: 700; font-size: 51px; }
  .services { font-weight: 800; font-size: 36px; }
  .brand-name {
    font-family: "Montserrat", sans-serif;
    font-weight: 800;
    font-size: 38px;
    fill: var(--ink-mark);
  }
</style>
</head>
<body>
<main class="canvas">
  <svg class="wrap-panel" viewBox="340 678 972 424" xmlns="http://www.w3.org/2000/svg" aria-label="Harbeck Restoration box truck side wrap">
    <defs>
      <linearGradient id="greyFill" x1="0" y1="0" x2="0" y2="1">
        <stop offset="0" stop-color="var(--grey-top)"/>
        <stop offset="1" stop-color="var(--grey-bottom)"/>
      </linearGradient>
      <linearGradient id="blueFill" x1="0" y1="0" x2="0" y2="1">
        <stop offset="0" stop-color="var(--blue-top)"/>
        <stop offset="1" stop-color="var(--blue-bottom)"/>
      </linearGradient>
    </defs>

    <rect class="panel-frame" x="340" y="678" width="972" height="424" fill="var(--frame)"/>
    <rect class="panel-grey" x="356" y="692" width="938" height="393" fill="url(#greyFill)"/>
    <path class="panel-stripe" d="M356 852 H685 V958 H1294 V985 H685 V876 H356 Z" fill="var(--stripe)"/>
    <path class="panel-blue" d="M356 876 H685 V985 H1294 V1085 H356 Z" fill="url(#blueFill)"/>

    <g class="brand-badge">
      <circle cx="685" cy="888" r="172" fill="var(--ink-light)" stroke="var(--stripe)" stroke-width="6"/>
      <text class="brand-name" x="685" y="878" text-anchor="middle">HARBECK</text>
      <text class="brand-name" x="685" y="922" text-anchor="middle" style="font-size:27px">RESTORATION</text>
    </g>

    <text class="wrap-text hours-number" x="378" y="790">24</text>
    <text class="wrap-text hours-label" x="381" y="810">HOUR SERVICE</text>

    <text class="wrap-text company-name" x="1075" y="802" text-anchor="middle">HARBECK</text>
    <text class="wrap-text company-name" x="1075" y="857" text-anchor="middle">RESTORATION</text>
    <text class="wrap-text company-phone" x="1075" y="917" text-anchor="middle">(702)555-0147</text>

    <text class="wrap-text services" x="1266" y="1046" text-anchor="end">•WATER • FIRE • MOLD</text>
  </svg>
</main>
</body>
</html>
```